Corporate Design für Veranstalter von Fundraising-Events zum Thema Naturschutz
Zielgruppe
Wir sind eine Organisation, die Fundraising Events zum Thema Naturschutz organisiert. Spenden gehen an internationale Naturschutzprojekte. Unsere Zielgruppe sind große Firmen, wie auch private Spender von jung bis alt.
Aufgabenstellung
Wir suchen ein hochwertiges Design, das auf internationaler Bühne Zuspruch findet. Unternehmenssprache ist Englisch, daher bitte jeglichen Text in englischer Sprache verfassen. Der Name unser Organisation ist Colina Brava, was grüner Schmetterling in Spanisch bedeutet. Unser Logo sollte daher einen grünen Schmetterling enthalten und die Farbe Grün (hellgrün-saftig) die dominante Farbe im Corporate Design sein. Je nach Design könnten wir uns als weitere Farbakzente erdige Töne vorstellen, vorrangig orange.

```html
<!DOCTYPE html>
<html lang="en">
<head>
<meta charset="utf-8">
<title>Colina Brava – Business Cards</title>
<link href="https://fonts.googleapis.com/css2?family=Raleway:wght@400;500&family=Open+Sans:wght@400;600&display=swap" rel="stylesheet">
<style>
  :root {
    --backdrop: #a4a4a4;
    --card-dark: #2f2f2f;
    --card-light: #474747;
    --leaf-green: #7cb82f;
    --leaf-green-deep: #5f9a1e;
    --text-light: #e6e6e6;
    --text-muted: #bdbdbd;
    --hairline: rgba(255,255,255,0.14);
  }
  * { margin: 0; padding: 0; box-sizing: border-box; }
  html, body { width: 1200px; height: 900px; overflow: hidden; }
  body {
    background: var(--backdrop);
    font-family: "Raleway", "Helvetica Neue", Arial, sans-serif;
    position: relative;
  }
  .card {
    position: absolute;
    top: 302px;
    width: 520px;
    height: 297px;
    background: radial-gradient(ellipse at 65% 35%, var(--card-light) 0%, var(--card-dark) 75%);
    overflow: hidden;
    box-shadow: 0 18px 40px rgba(0,0,0,0.22);
  }
  .card--contact { left: 50px; }
  .card--brand { left: 630px; }

  .card__decor { position: absolute; inset: 0; }

  .brand-block {
    position: absolute;
    text-align: center;
  }
  .brand-block__mark {
    display: block;
    margin: 0 auto 10px;
    border: 1.5px solid var(--leaf-green);
    border-radius: 50%;
  }
  .brand-block__name {
    color: var(--leaf-green);
    font-weight: 400;
    white-space: nowrap;
  }
  .brand-block__tagline {
    color: var(--text-light);
    font-weight: 400;
    white-space: nowrap;
  }

  .card--contact .brand-block { left: 40px; top: 92px; width: 190px; }
  .card--contact .brand-block__mark { width: 40px; height: 40px; }
  .card--contact .brand-block__name { font-size: 20px; letter-spacing: 0.5px; }
  .card--contact .brand-block__tagline { font-size: 9px; letter-spacing: 1.4px; margin-top: 2px; }

  .card--brand .brand-block { left: 0; right: 0; top: 70px; }
  .card--brand .brand-block__mark { width: 70px; height: 70px; margin-bottom: 18px; }
  .card--brand .brand-block__name { font-size: 25px; letter-spacing: 0.8px; }
  .card--brand .brand-block__tagline { font-size: 11px; letter-spacing: 1.8px; margin-top: 3px; }

  .contact {
    position: absolute;
    left: 292px;
    top: 50px;
    font-family: "Open Sans", Arial, sans-serif;
    color: var(--text-light);
  }
  .contact__name {
    font-family: "Raleway", Arial, sans-serif;
    font-size: 19px;
    font-weight: 500;
    letter-spacing: 3px;
  }
  .contact__role {
    color: var(--leaf-green);
    font-size: 8.5px;
    font-weight: 600;
    margin: 3px 0 10px;
  }
  .contact__row {
    display: flex;
    align-items: flex-start;
    gap: 8px;
    font-size: 8.5px;
    line-height: 1.3;
    color: var(--text-muted);
    margin-bottom: 9px;
  }
  .contact__icon { width: 10px; height: 10px; flex: none; margin-top: 1px; }

  .card__band {
    position: absolute;
    left: 0; right: 0; bottom: 0;
    height: 8px;
    background: var(--leaf-green);
  }
</style>
</head>
<body>

  <!-- Contact side -->
  <section class="card card--contact" aria-label="Business card, contact side">
    <svg class="card__decor" viewBox="0 0 520 297" aria-hidden="true">
      <path d="M0 297 L0 289 L520 222 L520 297 Z" fill="var(--leaf-green)"/>
      <path d="M0 297 L0 293 L520 230 L520 297 Z" fill="var(--card-dark)"/>
      <path d="M0 297 L0 296 L520 236 L520 297 Z" fill="var(--leaf-green-deep)"/>
      <path d="M150 10 C40 60 40 220 240 260" fill="none" stroke="var(--leaf-green)" stroke-width="1.4"/>
      <path d="M170 4 C60 70 70 235 280 250" fill="none" stroke="var(--leaf-green)" stroke-width="1"/>
      <line x1="272" y1="40" x2="272" y2="215" stroke="var(--hairline)" stroke-width="1"/>
    </svg>

    <div class="brand-block">
      <span class="brand-block__mark"></span>
      <div class="brand-block__name">COLINA BRAVA</div>
      <div class="brand-block__tagline">NATURE CONSERVATION</div>
    </div>

    <div class="contact">
      <div class="contact__name">FULL NAME</div>
      <div class="contact__role">Position</div>
      <div class="contact__row">
        <svg class="contact__icon" viewBox="0 0 10 10"><path d="M5 0.5a3.2 3.2 0 0 0-3.2 3.2C1.8 6 5 9.5 5 9.5S8.2 6 8.2 3.7A3.2 3.2 0 0 0 5 .5Zm0 4.4a1.2 1.2 0 1 1 0-2.4 1.2 1.2 0 0 1 0 2.4Z" fill="var(--leaf-green)"/></svg>
        <span>Building Street<br>City Country</span>
      </div>
      <div class="contact__row">
        <svg class="contact__icon" viewBox="0 0 10 10"><path d="M2.3 .8 3.8 2.6 3 3.8c.6 1.3 1.8 2.5 3.2 3.2l1.2-.8 1.8 1.5-.9 1.3C4.6 8.8 1.2 5.4.9 1.7Z" fill="var(--leaf-green)"/></svg>
        <span>+12 345 6789<br>+12 345 6789</span>
      </div>
      <div class="contact__row">
        <svg class="contact__icon" viewBox="0 0 10 10"><rect x="0.5" y="2" width="9" height="6" fill="var(--leaf-green)"/><path d="M0.5 2 5 5.5 9.5 2" fill="none" stroke="var(--card-dark)" stroke-width="0.8"/></svg>
        <span>www.colinabrava.org<br>info@colinabrava.org</span>
      </div>
    </div>
  </section>

  <!-- Brand side -->
  <section class="card card--brand" aria-label="Business card, brand side">
    <div class="brand-block">
      <span class="brand-block__mark"></span>
      <div class="brand-block__name">COLINA BRAVA</div>
      <div class="brand-block__tagline">NATURE CONSERVATION</div>
    </div>
    <div class="card__band"></div>
  </section>

</body>
</html>
```